fizzy drinks label design

I want to design fizzy drink label for 3 flavors : black grapes, red apple and mojito, band name kestrola, product name KOLTA , product will be in plastic bottle, label size 198 mm X 66mm

```html
<!DOCTYPE html>
<html lang="en">
<head>
<meta charset="UTF-8">
<title>kestrola KOLTA – Black Grapes label</title>
<link rel="stylesheet" href="https://fonts.googleapis.com/css2?family=Montserrat:wght@500;600;700;800&family=Arimo:wght@400;700&family=Dancing+Script:wght@600&display=swap">
<style>
  :root {
    --page-bg: #6e3f92;
    --label-dark: #3b1a58;
    --label-mid: #5c2d82;
    --label-glow: #7a47a3;
    --ink-white: #ffffff;
    --ink-soft: #ece2f5;
    --panel-white: #ffffff;
    --panel-ink: #3f2f78;
    --panel-bar: #4a3d85;
    --grape-deep: #2c2145;
    --grape-mid: #4b4478;
    --leaf: #7cc63a;
    --leaf-deep: #4f9a2a;
  }
  * { box-sizing: border-box; margin: 0; padding: 0; }
  html, body { width: 1200px; height: 1200px; overflow: hidden; }
  body {
    background: var(--page-bg);
    font-family: "Montserrat", sans-serif;
    position: relative;
  }
  .label {
    position: absolute;
    left: 30px; top: 410px;
    width: 1140px; height: 380px;
    background: radial-gradient(ellipse at 50% 55%, var(--label-glow) 0%, var(--label-mid) 45%, var(--label-dark) 100%);
    box-shadow: 0 6px 24px rgba(30, 10, 50, 0.45);
    overflow: hidden;
  }

  /* Nutrition panel */
  .nutrition {
    position: absolute;
    left: 43px; top: 46px;
    width: 293px; height: 288px;
    background: var(--panel-white);
    color: var(--panel-ink);
    font-family: "Arimo", sans-serif;
    padding: 7px 7px 0 8px;
  }
  .nutrition h2 {
    font-family: "Montserrat", sans-serif;
    font-weight: 800;
    font-size: 27px;
    letter-spacing: 0.6px;
    text-align: center;
    line-height: 1.1;
    margin-bottom: 2px;
  }
  .nutrition .serving { font-weight: 700; font-size: 10.5px; line-height: 12.5px; padding-left: 3px; }
  .nutrition .bar { height: 9px; background: var(--panel-bar); margin: 3px 0; }
  .nutrition .row {
    display: flex; justify-content: space-between;
    font-size: 10.5px; line-height: 12.3px;
    border-bottom: 1px solid var(--panel-bar);
    padding: 0 3px;
  }
  .nutrition .row.plain { border-bottom: none; }
  .nutrition .row.small { font-size: 8px; line-height: 10px; font-weight: 700; }
  .nutrition .row.right { justify-content: flex-end; font-weight: 700; }
  .nutrition .row b { font-weight: 700; }
  .nutrition .row.sub span:first-child { padding-left: 23px; }
  .nutrition .note { font-size: 8.2px; line-height: 10px; padding: 0 3px; }

  /* Centre brand */
  .leaf-art {
    position: absolute; left: 383px; top: 4px;
    width: 69px; height: 50px;
    border-radius: 50%;
    background: radial-gradient(circle at 45% 40%, #a6dc5a 0%, var(--leaf-deep) 100%);
  }
  .brand {
    position: absolute; left: 440px; top: 22px; width: 258px;
    text-align: center; color: var(--ink-white);
  }
  .brand .maker {
    font-weight: 800; font-size: 21px; line-height: 1.1;
    display: inline-flex; align-items: center; gap: 6px;
  }
  .brand .maker i {
    display: inline-block; width: 10px; height: 10px;
    border-radius: 50%; background: var(--ink-white);
  }
  .brand .product {
    font-weight: 800; font-size: 58px; line-height: 1;
    letter-spacing: 2px; margin-top: 4px;
  }
  .brand .flavour {
    font-family: "Dancing Script", cursive;
    font-size: 22px; line-height: 1.1; margin-top: 2px;
    transform: rotate(-8deg);
  }
  .grape-art {
    position: absolute; left: 498px; top: 156px;
    width: 140px; height: 182px;
    border-radius: 45% 45% 48% 48% / 35% 35% 60% 60%;
    background: radial-gradient(ellipse at 50% 20%, #6aa840 0%, var(--grape-mid) 38%, var(--grape-deep) 100%);
    opacity: 0.9;
  }
  .volume {
    position: absolute; left: 671px; top: 347px;
    color: var(--ink-white); font-weight: 700; font-size: 13px;
  }
  .new-badge {
    position: absolute; left: 710px; top: 338px;
    width: 44px; height: 26px; border-radius: 6px;
    background: var(--leaf);
  }

  /* Right info */
  .info {
    position: absolute; left: 791px; top: 30px; width: 324px;
    color: var(--ink-white);
  }
  .info h3 {
    font-weight: 700; font-size: 22px; letter-spacing: 0.5px; line-height: 1.2;
    margin-bottom: 6px;
  }
  .info p {
    font-size: 10.3px; line-height: 12.2px; text-align: justify;
    color: var(--ink-soft); font-weight: 500;
  }
  .info .block + .block { margin-top: 16px; }
  .company {
    position: absolute; right: 25px; top: 272px;
    text-align: right; color: var(--ink-white);
  }
  .company h4 { font-weight: 600; font-size: 20px; letter-spacing: 0.5px; margin-bottom: 6px; }
  .company p { font-size: 11px; line-height: 13.8px; font-weight: 500; }
</style>
</head>
<body>
  <section class="label" aria-label="kestrola KOLTA Black Grapes bottle label">

    <div class="nutrition">
      <h2>Nutrition Facts</h2>
      <p class="serving">Serving Size 2.22oz</p>
      <p class="serving">Servings per Container 1</p>
      <div class="bar"></div>
      <div class="row small plain"><span>Amount Per Serving</span></div>
      <div class="row"><span><b>Calories</b> 385</span><span><b>Calories from Fat</b> 249</span></div>
      <div class="bar"></div>
      <div class="row right plain"><span>% Daily Values*</span></div>
      <div class="row"><span><b>Total Fat</b> 27.6g</span><span>42.5%</span></div>
      <div class="row sub"><span>Saturated Fat 0g</span><span>0%</span></div>
      <div class="row sub"><span>Trans Fat 0g</span><span></span></div>
      <div class="row"><span><b>Cholesterol</b> 0mg</span><span>0%</span></div>
      <div class="row"><span><b>Sodium</b> 30mg</span><span>1.3%</span></div>
      <div class="row"><span><b>Total Carbohydrate</b> 29.7g</span><span>10%</span></div>
      <div class="row sub"><span>Dietary Fiber 0g</span><span>0%</span></div>
      <div class="row sub"><span>Sugars 29.7g</span><span></span></div>
      <div class="row plain"><span><b>Protein</b> 4.4g</span><span></span></div>
      <div class="bar"></div>
      <p class="note">* Percent Daily Values are based on a 2,000 calories diet. Your Daily Values may be higher or lower depending on your calories needs.</p>
    </div>

    <div class="leaf-art" role="img" aria-label="Green grape leaf illustration"></div>

    <div class="brand">
      <div class="maker"><i></i>kestrola</div>
      <div class="product">KOLTA</div>
      <div class="flavour">Black Grapes</div>
    </div>

    <div class="grape-art" role="img" aria-label="Illustration of a bunch of black grapes topped with a green leaf"></div>

    <span class="volume">330m</span>
    <span class="new-badge" aria-hidden="true"></span>

    <div class="info">
      <div class="block">
        <h3>DIRECTIONS</h3>
        <p>Lorem ipsum dolor sit amet, consectetur adipiscing elit, sed do eiusmod tempor incididunt ut labore et dolore magna aliqua. Vivamus at augue eget arcu. Sed risus pretium quam vulputate dignissim suspendisse in est ante. Sed augue lacus viverra vitae congue eu. Dignissim enim sit amet venenatis urna cursus eget et. Ultrices vitae auctor eu augue.</p>
      </div>
      <div class="block">
        <h3>INGREDIENTS</h3>
        <p>Lorem ipsum dolor sit amet, consectetur adipiscing elit, sed do eiusmod tempor incididunt ut labore et dolore magna aliqua. Vivamus at augue eget arcu. Sed risus pretium quam vulputate dignissim suspendisse in est ante. Sed augue lacus viverra vitae congue eu. Dignissim enim sit amet venenatis urna cursus eget et. Ultrices vitae auctor eu augue.</p>
      </div>
    </div>

    <div class="company">
      <h4>COMPANY NAME</h4>
      <p>123 Address Name</p>
      <p>Street Name</p>
      <p>Phone: 0123456789</p>
      <p>WWW.com</p>
    </div>

  </section>
</body>
</html>
```